Harrowgate Supply Group Business Card Design

The Business Card will be one side only with Harrowgate Supplies Group Logo
Card should have:
Name
Title
Office phone Number
Cell Number
email address
Website
Street Address
Our Slogan is Rugged and Reliable
Looking for something that stands out from other business cards

Target Market(s)

Heavy equipment Lease Company

```html
<!DOCTYPE html>
<html lang="en">
<head>
<meta charset="utf-8">
<title>Harrowgate Supplies Group Business Card</title>
<link href="https://fonts.googleapis.com/css2?family=Montserrat:wght@600;700&family=Roboto:wght@400;500&display=swap" rel="stylesheet">
<style>
  :root {
    --backdrop: #1d1d1d;
    --navy: #2a2a78;
    --red: #d01f3c;
    --white: #ffffff;
    --ink: #1f1f2e;
    --rule: #2a2a50;
  }
  * { box-sizing: border-box; margin: 0; padding: 0; }
  html, body { width: 1200px; height: 900px; overflow: hidden; background: var(--backdrop); }
  .canvas { position: relative; width: 1200px; height: 900px; }
  .card {
    position: absolute; left: 290px; width: 620px; height: 354px;
    font-family: "Roboto", Arial, sans-serif; border-radius: 3px;
  }
  .card--front { top: 70px; background: var(--navy); }
  .card--back { top: 476px; background: var(--white); }

  .brand { display: flex; align-items: center; gap: 12px; }
  .brand__mark { width: 22px; height: 22px; border-radius: 50%; flex: none; }
  .brand__name {
    font-family: "Montserrat", Arial, sans-serif; font-weight: 700;
    color: var(--red); letter-spacing: 0.5px; text-transform: uppercase;
    white-space: nowrap;
  }

  .front__brand { position: absolute; left: 0; right: 0; top: 140px; justify-content: center; }
  .front__brand .brand__mark { background: var(--white); width: 30px; height: 30px; }
  .front__brand .brand__name { font-size: 27px; }
  .front__rule { position: absolute; left: 150px; right: 150px; top: 192px; height: 2px; background: var(--white); }
  .front__slogan {
    position: absolute; left: 0; right: 0; top: 236px; text-align: center;
    color: var(--white); font-size: 15px; letter-spacing: 1px;
  }

  .back__brand { position: absolute; left: 40px; top: 58px; }
  .back__brand .brand__mark { background: var(--navy); width: 20px; height: 20px; }
  .back__brand .brand__name { font-size: 17px; }
  .back__address {
    position: absolute; right: 40px; top: 46px; width: 170px; text-align: right;
    color: var(--ink); font-size: 12px; line-height: 1.45; font-style: normal;
  }
  .back__rule { position: absolute; left: 40px; right: 40px; top: 112px; height: 1px; background: var(--rule); }
  .person { position: absolute; left: 40px; top: 140px; }
  .person__name {
    font-family: "Montserrat", Arial, sans-serif; font-weight: 700;
    color: var(--red); font-size: 26px; letter-spacing: 0.5px;
  }
  .person__title { color: var(--ink); font-size: 15px; margin-top: 2px; }
  .contact__rule { position: absolute; left: 40px; width: 250px; top: 214px; height: 1px; background: var(--rule); }
  .contact { position: absolute; left: 40px; top: 228px; list-style: none; }
  .contact__item {
    display: flex; align-items: center; gap: 10px;
    color: var(--ink); font-size: 15px; line-height: 1; margin-bottom: 9px;
  }
  .contact__icon { width: 14px; height: 14px; fill: var(--navy); flex: none; }
</style>
</head>
<body>
<div class="canvas">
  <section class="card card--front">
    <div class="brand front__brand">
      <span class="brand__mark"></span>
      <span class="brand__name">Harrowgate Supplies Group</span>
    </div>
    <div class="front__rule"></div>
    <p class="front__slogan">Rugged and Reliable</p>
  </section>

  <section class="card card--back">
    <div class="brand back__brand">
      <span class="brand__mark"></span>
      <span class="brand__name">Harrowgate Supplies Group</span>
    </div>
    <address class="back__address">
      4120<br>Cedar Ridge Blvd Ste. B<br>Marlow, TX 77502
    </address>
    <div class="back__rule"></div>
    <div class="person">
      <div class="person__name">DANIEL REEVES</div>
      <div class="person__title">Director</div>
    </div>
    <div class="contact__rule"></div>
    <ul class="contact">
      <li class="contact__item">
        <svg class="contact__icon" viewBox="0 0 14 14"><rect x="3" y="0" width="8" height="14" rx="1.5"/><rect x="4.5" y="2" width="5" height="8" fill="#fff"/></svg>
        012 555 0147
      </li>
      <li class="contact__item">
        <svg class="contact__icon" viewBox="0 0 14 14"><path d="M3 1l2.5 0 1 3-1.5 1.2a8 8 0 0 0 3.8 3.8L10 7.5l3 1V11a2 2 0 0 1-2 2A10 10 0 0 1 1 3a2 2 0 0 1 2-2z"/></svg>
        123 555 0192
      </li>
      <li class="contact__item">
        <svg class="contact__icon" viewBox="0 0 14 14"><rect x="0" y="2.5" width="14" height="9" rx="1"/><path d="M0.5 3l6.5 5 6.5-5" stroke="#fff" stroke-width="1.2" fill="none"/></svg>
        info@harrowgatesupplies.com
      </li>
      <li class="contact__item">
        <svg class="contact__icon" viewBox="0 0 14 14"><circle cx="7" cy="7" r="6.5"/><path d="M0.5 7h13M7 0.5v13M7 0.5c-3 3.5-3 9.5 0 13M7 0.5c3 3.5 3 9.5 0 13" stroke="#fff" stroke-width="0.9" fill="none"/></svg>
        www.harrowgatesupplies.com
      </li>
    </ul>
  </section>
</div>
</body>
</html>
```